K9 Orbit needs a business card designed

We need a business card designed for K9 Orbit, an expansion of K9 Systems Pty Ltd (www.k9systems.com.au)

We provide high quality professional services for the Australian space industry. Our clients include the Southern Launch Bureau and companies working in the space industry. We identify people with space related skills both locally and internationally who are then contracted by clients to create products and support space launch activities.

Colours to be used:
- Navy blue #000080
- Rocket metallic #8A7F8D
- Platinum #E5E4E2
- Black #000000
- White #FFFFFF

*Front of the card*
I have attached our K9 Orbit logo, which needs to be the main item on the card. The 'Space' text should be placed to the right of the 'K9' part rather than below, similar to the attached K9 Systems card, which this card should match.

If subtext is included, however, it should read ‘Labour Hire • Consultancy • Project Delivery’ rather than the ‘Design • Build • Test • Maintain’ of the K9 Systems card.

A black background (rather than blue background in the K9 Systems card) might be good, with a white pattern as in the K9 Systems card. If colour is used, the logo should be in its standard colours (as provided for the K9 Orbit logo).

*Back of the card*
Include a smaller K9 Orbit logo on the back.

We need the following details for K9 Orbit personnel (as a template for entry):
- Name
- Company Position
- Mobile Number
- Email
- Office Address
- Include the K9 Orbit website: www.k9orbit.com.au

Overall, we'd like to see a design that communicates the adventure of space, professional integrity, and customer service. We look forward to seeing what you can come up with.

Target Market(s)

We provide high quality professional services for the Australian space industry. Our clients include the Southern Launch Bureau and companies working in the space industry.

Contact Information for Business Card

- Name
- Company Position
- Mobile Number
- Email
- Office Address

Requirements
Must have
• See project description.

```html
<!DOCTYPE html>
<html lang="en">
<head>
<meta charset="UTF-8">
<title>K9 Orbit Business Card</title>
<link href="https://fonts.googleapis.com/css2?family=Montserrat:wght@400;500;600;800&display=swap" rel="stylesheet">
<style>
  :root {
    --black: #000000;
    --white: #ffffff;
    --platinum: #e5e4e2;
    --silver-light: #e9eeee;
    --silver-mid: #c9cfd0;
    --silver-dark: #aeb4b6;
    --stage: #232323;
    --ink: #111111;
  }
  * { box-sizing: border-box; margin: 0; padding: 0; }
  html, body {
    width: 1200px; height: 780px; overflow: hidden;
    background: var(--stage);
    font-family: "Montserrat", sans-serif;
  }
  .canvas {
    width: 1200px; height: 780px;
    display: flex; align-items: center; justify-content: center; gap: 40px;
  }
  .card {
    position: relative; width: 560px; height: 320px; overflow: hidden;
    box-shadow: 0 18px 40px rgba(0,0,0,.55);
  }
  .card-bg { position: absolute; inset: 0; width: 100%; height: 100%; }

  /* Front */
  .front-content {
    position: absolute; inset: 0;
    display: flex; flex-direction: column; align-items: center; justify-content: center;
    color: var(--white);
  }
  .lockup { display: flex; align-items: center; gap: 22px; }
  .brand-name {
    font-weight: 600; font-size: 30px; letter-spacing: 3px; color: var(--white);
    display: flex; align-items: center; gap: 10px;
  }
  .brand-dot { width: 10px; height: 10px; border-radius: 50%; background: var(--white); }
  .divider { width: 1px; height: 62px; background: var(--white); }
  .sister-name { font-weight: 400; font-size: 28px; color: var(--white); }
  .tagline {
    margin-top: 26px; font-size: 11.5px; font-weight: 500; letter-spacing: 3.2px;
  }

  /* Back */
  .back-logo {
    position: absolute; left: 34px; top: 36px;
    font-weight: 600; font-size: 20px; letter-spacing: 2px; color: var(--white);
    display: flex; align-items: center; gap: 8px;
  }
  .back-logo .brand-dot { width: 8px; height: 8px; }
  .identity {
    position: absolute; right: 30px; top: 40px; text-align: right; color: var(--ink);
  }
  .person-name {
    display: inline-block; font-weight: 800; font-size: 21px; line-height: 1.05;
    padding-right: 10px; border-right: 4px solid var(--ink);
  }
  .designation {
    margin-top: 8px; font-size: 8.5px; letter-spacing: 3.4px; font-weight: 500; color: #333;
  }
  .contacts {
    position: absolute; right: 26px; top: 150px; list-style: none; color: var(--ink);
  }
  .contact {
    display: flex; align-items: center; justify-content: flex-end; gap: 10px;
    font-size: 10.5px; font-weight: 600; line-height: 1.25; text-align: right;
    margin-bottom: 10px;
  }
  .icon {
    flex: none; width: 20px; height: 20px; border-radius: 50%; background: var(--black);
    display: flex; align-items: center; justify-content: center;
  }
  .icon svg { width: 11px; height: 11px; }
</style>
</head>
<body>
<main class="canvas">

  <section class="card card-front" aria-label="Card front">
    <svg class="card-bg" viewBox="0 0 560 320" preserveAspectRatio="none" aria-hidden="true">
      <defs>
        <linearGradient id="frontSilver" x1="0" y1="0" x2="1" y2="1">
          <stop offset="0" stop-color="#e9eeee"/>
          <stop offset="1" stop-color="#c9cfd0"/>
        </linearGradient>
      </defs>
      <rect width="560" height="320" fill="url(#frontSilver)"/>
      <path d="M118,0 L560,0 L560,92 Q530,250 468,320 L38,320 Q42,120 118,0 Z" fill="#000"/>
    </svg>
    <div class="front-content">
      <div class="lockup">
        <div class="brand-name"><span class="brand-dot"></span>K9 ORBIT</div>
        <span class="divider"></span>
        <div class="sister-name">K9 Systems</div>
      </div>
      <p class="tagline">Labour Hire • Consultancy • Project Delivery</p>
    </div>
  </section>

  <section class="card card-back" aria-label="Card back">
    <svg class="card-bg" viewBox="0 0 560 320" preserveAspectRatio="none" aria-hidden="true">
      <defs>
        <linearGradient id="backSilver" x1="0" y1="0" x2="1" y2="1">
          <stop offset="0" stop-color="#aeb4b6"/>
          <stop offset=".5" stop-color="#dde3e3"/>
          <stop offset="1" stop-color="#b9bfc1"/>
        </linearGradient>
      </defs>
      <rect width="560" height="320" fill="url(#backSilver)"/>
      <path d="M0,0 L238,0 L352,226 Q368,268 318,320 L0,320 Z" fill="#000"/>
    </svg>

    <div class="back-logo"><span class="brand-dot"></span>K9 ORBIT</div>

    <div class="identity">
      <div class="person-name">YOUR<br>NAMEHERE</div>
      <p class="designation">YOUR DESIGNATION</p>
    </div>

    <ul class="contacts">
      <li class="contact">+61 4123 555 010
        <span class="icon"><svg viewBox="0 0 24 24"><path fill="#fff" d="M6.6 10.8a15 15 0 0 0 6.6 6.6l2.2-2.2c.3-.3.7-.4 1-.2 1.1.4 2.3.6 3.6.6.6 0 1 .4 1 1V20c0 .6-.4 1-1 1A17 17 0 0 1 3 4c0-.6.4-1 1-1h3.5c.6 0 1 .4 1 1 0 1.3.2 2.5.6 3.6.1.3 0 .7-.2 1z"/></svg></span>
      </li>
      <li class="contact">youremailgoeshere@k9o.com
        <span class="icon"><svg viewBox="0 0 24 24"><rect x="3" y="6" width="18" height="12" fill="none" stroke="#fff" stroke-width="2"/><path d="M3 6l9 7 9-7" fill="none" stroke="#fff" stroke-width="2"/></svg></span>
      </li>
      <li class="contact">Level 3, 58 Harbour St<br>Port Lindell VIC 3210
        <span class="icon"><svg viewBox="0 0 24 24"><path fill="#fff" d="M12 2a7 7 0 0 0-7 7c0 5 7 13 7 13s7-8 7-13a7 7 0 0 0-7-7zm0 9.5A2.5 2.5 0 1 1 12 6.5a2.5 2.5 0 0 1 0 5z"/></svg></span>
      </li>
      <li class="contact">www.k9orbit.com.au
        <span class="icon"><svg viewBox="0 0 24 24" fill="none" stroke="#fff" stroke-width="2"><circle cx="12" cy="12" r="9"/><path d="M3 12h18M12 3c3 3 3 15 0 18M12 3c-3 3-3 15 0 18"/></svg></span>
      </li>
    </ul>
  </section>

</main>
</body>
</html>
```